Venmoral Baby Collection

We are creating the label for baby skin care products for our existing skin care brand called Venmoral. we want to play on sophistication of Venmoral current labelling and change to include kids/baby look and feel but keeping the up market style. We will have full range of different products like
1.Shampoo and Body Wash
2. Healing Cream
3. Nappy Rush Cream
4. Baby Massage Gel
5.Baby Bubble Bath
6.Baby Soothing Skin Lotion

Target Market(s)

Our target market are customers in Australia and Asia looking to purchase quality skin care products for their new born babies and young children

Industry/Entity Type

Skin care

Requirements
Must have
• some children look combined with an existing Venmoral brand
Nice to have
• maybe some baby toys and letters around the main name Venmoral

```html
<!DOCTYPE html>
<html lang="en">
<head>
<meta charset="UTF-8">
<title>Venmoral Baby Bubble Bath Label</title>
<link rel="stylesheet" href="https://fonts.googleapis.com/css2?family=Libre+Baskerville:wght@700&family=Fredoka:wght@400;600;700&display=swap">
<style>
  :root {
    --page-bg: #f4f4f4;
    --label-top: #c9e8ef;
    --label-bottom: #e4f3f6;
    --cloud: rgba(255, 255, 255, 0.55);
    --title-blue: #2f7db0;
    --bath-blue: #3a7fa8;
    --brand-white: #f2f9fb;
    --banner-blue: #2b6e97;
    --banner-text: #ffffff;
    --art-top: #f3dcb9;
    --art-mid: #eed8de;
    --art-bottom: #cfe6f0;
  }
  html, body {
    margin: 0;
    width: 1200px;
    height: 1200px;
    overflow: hidden;
    background: var(--page-bg);
  }
  .label {
    position: absolute;
    left: 100px;
    top: 171px;
    width: 1000px;
    height: 858px;
    background:
      radial-gradient(ellipse 60% 35% at 20% 85%, var(--cloud), transparent 70%),
      radial-gradient(ellipse 50% 30% at 85% 70%, var(--cloud), transparent 70%),
      linear-gradient(180deg, var(--label-top) 0%, var(--label-bottom) 100%);
    overflow: hidden;
  }
  .brand-name {
    position: absolute;
    top: 72px;
    left: 0;
    width: 915px;
    text-align: center;
    font-family: "Libre Baskerville", serif;
    font-weight: 700;
    font-size: 34px;
    color: var(--brand-white);
    letter-spacing: 1px;
    margin: 0;
  }
  .product-title {
    position: absolute;
    left: 0;
    top: 0;
    width: 1000px;
    height: 320px;
  }
  .product-title .title-arc {
    font-family: "Fredoka", "Arial Rounded MT Bold", sans-serif;
    font-weight: 700;
    font-size: 64px;
    fill: var(--title-blue);
    letter-spacing: 1px;
  }
  .product-title .title-sub {
    font-family: "Fredoka", sans-serif;
    font-weight: 400;
    font-size: 38px;
    fill: var(--bath-blue);
    letter-spacing: 2px;
  }
  .bath-art {
    position: absolute;
    left: 190px;
    top: 310px;
    width: 548px;
    height: 441px;
    border-radius: 40px;
    background: linear-gradient(180deg, var(--art-top) 0%, var(--art-mid) 50%, var(--art-bottom) 100%);
  }
  .usage-banner {
    position: absolute;
    left: 294px;
    top: 806px;
    width: 374px;
    height: 44px;
    background: var(--banner-blue);
    clip-path: polygon(0 0, 100% 0, 97% 50%, 100% 100%, 0 100%, 3% 50%);
    display: flex;
    align-items: center;
    justify-content: center;
    font-family: "Fredoka", sans-serif;
    font-weight: 600;
    font-size: 21px;
    color: var(--banner-text);
    letter-spacing: 0.5px;
  }
</style>
</head>
<body>
  <section class="label">
    <p class="brand-name">Venmoral</p>

    <svg class="product-title" viewBox="0 0 1000 320" aria-label="Baby Bubble Bath">
      <defs>
        <path id="title-curve" d="M 215 250 Q 460 140 705 250"/>
      </defs>
      <text class="title-arc">
        <textPath href="#title-curve" startOffset="50%" text-anchor="middle">BABY BUBBLE</textPath>
      </text>
      <text class="title-sub" x="458" y="262" text-anchor="middle">-BATH-</text>
    </svg>

    <div class="bath-art" role="img" aria-label="Watercolour illustration of baby animals bathing together in a bubble-filled tub"></div>

    <div class="usage-banner">FOR EVERYDAY USE &nbsp;·&nbsp; 500ML</div>
  </section>
</body>
</html>
```